LED panel tester - hand-held test tool - simple label required

I have designed a product to test the LED panels of a road-side variable message sign (VMS). I don't expect to sell too many of these but thought it would look professional if it had a proper label.

I need a label designed for this hand-held test equipment. Attached is the positional layout of all the switches and text. I have also included a photo of the product.

A simple Google image search of "hand-held test tool" shows that it doesn't have to be fancy but rather functional.

I would like to put branding on the bottom 1/5th and have the option to interchange the brand if I ever get approached by one of the manufacturers of these signs. Initially it will just have a link to my website (TallowbrookWorks.com.au) right down at the bottom.

```html
<!DOCTYPE html>
<html lang="en">
<head>
<meta charset="utf-8">
<title>VMS Panel Tester – Label Options</title>
<link rel="stylesheet" href="https://fonts.googleapis.com/css2?family=Montserrat:wght@400;500;600;800&family=Open+Sans:wght@400&display=swap">
<style>
  :root {
    --canvas: #ffffff;
    --panel-dark: #0d0d0d;
    --panel-mid: #1c1c1c;
    --brand-red: #dc0000;
    --switch: #ffffff;
    --label-red: #dc0000;
    --label-green: #55b530;
    --label-orange: #ee7d10;
    --label-white: #ffffff;
    --label-blue: #1428e6;
    --label-grey: #b4b4b4;
    --label-muted: #9a9a9a;
    --ink: #111111;
  }
  html, body {
    margin: 0;
    padding: 0;
    width: 1200px;
    height: 991px;
    overflow: hidden;
    background: var(--canvas);
  }
  .sheet {
    position: relative;
    width: 1200px;
    height: 991px;
  }
  .label {
    position: absolute;
    top: 81px;
    width: 454px;
    height: 841px;
    display: block;
  }
  .label--mono { left: 90px; }
  .label--banded { left: 623px; }

  .label__title {
    font-family: "Montserrat", sans-serif;
    font-weight: 800;
    font-size: 37px;
    letter-spacing: -0.5px;
  }
  .label--mono .label__title { fill: var(--brand-red); }
  .label--banded .label__title { fill: #ffffff; }

  .control-name {
    font-family: "Montserrat", sans-serif;
    font-weight: 600;
    font-size: 19px;
  }
  .control-name--power { font-weight: 400; font-size: 20px; }
  .label--mono .control-name--red { fill: var(--label-red); }
  .label--mono .control-name--green { fill: var(--label-green); }
  .label--mono .control-name--orange { fill: var(--label-orange); }
  .label--mono .control-name--white { fill: var(--label-white); }
  .label--mono .control-name--blue { fill: var(--label-blue); }
  .label--mono .control-name--speed { fill: var(--label-grey); }
  .label--mono .control-name--power { fill: var(--label-white); }
  .label--banded .control-name { fill: var(--label-muted); }

  .switch-hole { fill: var(--switch); }

  .label__web {
    font-family: "Open Sans", sans-serif;
    font-weight: 400;
    font-size: 26px;
    fill: #ffffff;
  }

  .option-tag {
    position: absolute;
    top: 842px;
    font-family: "Montserrat", sans-serif;
    font-weight: 800;
    font-size: 12px;
    color: var(--ink);
    writing-mode: vertical-rl;
    transform: rotate(180deg);
    letter-spacing: 0.2px;
  }
  .option-tag--one { left: 557px; }
  .option-tag--two { left: 1101px; }
</style>
</head>
<body>
<main class="sheet">

  <svg class="label label--mono" viewBox="0 0 454 841" aria-label="Label option one: black panel">
    <defs>
      <radialGradient id="mono-surface" cx="50%" cy="40%" r="75%">
        <stop offset="0" stop-color="#1a1a1a"/>
        <stop offset="1" stop-color="#0a0a0a"/>
      </radialGradient>
    </defs>
    <rect class="label__surface" width="454" height="841" fill="url(#mono-surface)" role="img" aria-label="Dark hexagon carbon texture"/>
    <text class="label__title" x="227" y="56" text-anchor="middle">VMS PANEL TESTER</text>

    <g class="switch-column">
      <circle class="switch-hole" cx="225" cy="148" r="24"/>
      <circle class="switch-hole" cx="225" cy="203" r="24"/>
      <circle class="switch-hole" cx="225" cy="266" r="24"/>
      <circle class="switch-hole" cx="225" cy="329" r="24"/>
      <circle class="switch-hole" cx="225" cy="390" r="24"/>
      <circle class="switch-hole" cx="225" cy="446" r="24"/>
    </g>
    <g class="control-names">
      <text class="control-name control-name--red" x="278" y="158">RED</text>
      <text class="control-name control-name--green" x="278" y="218">GREEN</text>
      <text class="control-name control-name--orange" x="278" y="279">ORANGE</text>
      <text class="control-name control-name--white" x="278" y="339">WHITE</text>
      <text class="control-name control-name--blue" x="278" y="400">BLUE</text>
      <text class="control-name control-name--speed" x="278" y="460">SLOW</text>
      <text class="control-name control-name--speed" x="167" y="460" text-anchor="end">FAST</text>
    </g>

    <rect class="switch-hole power-switch" x="130" y="534" width="180" height="105"/>
    <text class="control-name control-name--power" x="335" y="597">POWER</text>

    <text class="label__web" x="227" y="817" text-anchor="middle">www.TallowbrookWorks.com.au</text>
  </svg>
  <div class="option-tag option-tag--one">SAMPLE 1</div>

  <svg class="label label--banded" viewBox="0 0 454 841" aria-label="Label option two: black panel with red bands">
    <defs>
      <radialGradient id="banded-surface" cx="50%" cy="45%" r="70%">
        <stop offset="0" stop-color="#222222"/>
        <stop offset="1" stop-color="#0c0c0c"/>
      </radialGradient>
    </defs>
    <rect class="label__surface" width="454" height="841" fill="url(#banded-surface)" role="img" aria-label="Dark brushed texture"/>
    <path class="brand-band brand-band--top" d="M0 0 H454 V60 Q227 112 0 60 Z" fill="var(--brand-red)"/>
    <path class="brand-band brand-band--bottom" d="M0 791 Q227 741 454 791 V841 H0 Z" fill="var(--brand-red)"/>
    <text class="label__title" x="227" y="56" text-anchor="middle">VMS PANEL TESTER</text>

    <g class="switch-column">
      <circle class="switch-hole" cx="225" cy="148" r="24"/>
      <circle class="switch-hole" cx="225" cy="203" r="24"/>
      <circle class="switch-hole" cx="225" cy="266" r="24"/>
      <circle class="switch-hole" cx="225" cy="329" r="24"/>
      <circle class="switch-hole" cx="225" cy="390" r="24"/>
      <circle class="switch-hole" cx="225" cy="446" r="24"/>
    </g>
    <g class="control-names">
      <text class="control-name" x="278" y="158">RED</text>
      <text class="control-name" x="278" y="218">GREEN</text>
      <text class="control-name" x="278" y="279">ORANGE</text>
      <text class="control-name" x="278" y="339">WHITE</text>
      <text class="control-name" x="278" y="400">BLUE</text>
      <text class="control-name" x="278" y="460">SLOW</text>
      <text class="control-name" x="167" y="460" text-anchor="end">FAST</text>
    </g>

    <rect class="switch-hole power-switch" x="130" y="534" width="180" height="105"/>
    <text class="control-name control-name--power" x="335" y="597">POWER</text>

    <text class="label__web" x="227" y="817" text-anchor="middle">www.TallowbrookWorks.com.au</text>
  </svg>
  <div class="option-tag option-tag--two">SAMPLE 2</div>

</main>
</body>
</html>
```